Poster for Kirtan Music Event

Design (3) 24" x 36" Posters

I have provided a sample a friend did in Australia: ( Picture No. 4 )

Use all the text on sample poster except the replacement changes below.

Replace with the following text as this is for different location:
Replacement Text:

Every Friday Night 7:00pm-8:30pm
Nohea Breath & Movement Loft
752 Wenmore St Paia

Free Kirtan Experience! or Free Event
Madhava Vani Prabhu & Friends

Optional Text:

A evening of music, singing of spiritual mantras, and refreshments

Bring flowers, musical instruments, friends, or just come with an open heart.

Meditate on transcendental sounds that provide rest for the mind & heart"

An evening of music & singing of sacred mantra's

```html
<!DOCTYPE html>
<html lang="en">
<head>
<meta charset="utf-8">
<title>Free Kirtan Experience</title>
<link rel="stylesheet" href="https://fonts.googleapis.com/css2?family=Alegreya:wght@700&family=Arimo:wght@700&family=Great+Vibes&display=swap">
<style>
  :root {
    --bg-deep: #5c0104;
    --bg-mid: #8e0a0e;
    --bg-hot: #a8141a;
    --cream: #f6e38c;
    --gold: #f2cc3e;
    --gold-bright: #ffe21a;
    --white: #ffffff;
    --band-dark: #3a1606;
    --band-warm: #b8742a;
  }
  * { margin: 0; padding: 0; box-sizing: border-box; }
  html, body { width: 800px; height: 1200px; overflow: hidden; background: var(--bg-deep); }
  .poster {
    position: relative;
    width: 800px;
    height: 1200px;
    overflow: hidden;
    background: radial-gradient(ellipse at 50% 35%, var(--bg-hot) 0%, var(--bg-mid) 45%, var(--bg-deep) 100%);
    font-family: "Arimo", Arial, sans-serif;
    font-weight: 700;
  }
  .mandala-ornament {
    position: absolute;
    left: 70px; top: 15px;
    width: 660px; height: 680px;
    border-radius: 50%;
    background: radial-gradient(circle at 50% 25%, rgba(176,22,138,0.55) 0%, rgba(176,22,138,0.3) 35%, rgba(201,154,28,0.35) 60%, rgba(201,154,28,0) 72%);
  }
  .devotional-illustration {
    position: absolute;
    left: 287px; top: 130px;
    width: 115px; height: 170px;
    border-radius: 50% 50% 45% 45%;
    background: linear-gradient(180deg, #e6c7a6 0%, #c8906a 60%, rgba(160,40,40,0.6) 100%);
  }
  .headline {
    position: absolute;
    left: 0; top: 320px;
    width: 800px; height: 130px;
    font-weight: 700;
  }
  .headline .word {
    position: absolute;
    top: 32px;
    font-family: "Alegreya", Georgia, serif;
    font-weight: 700;
    font-size: 55px;
    line-height: 1;
    color: var(--cream);
    white-space: nowrap;
  }
  .headline .free { left: 92px; }
  .headline .experience { left: 502px; }
  .headline .kirtan {
    position: absolute;
    left: 226px; top: 6px;
    font-family: "Great Vibes", cursive;
    font-weight: 400;
    font-size: 92px;
    line-height: 1;
    color: var(--cream);
    white-space: nowrap;
  }
  .performer-photo {
    position: absolute;
    left: 267px; top: 447px;
    width: 268px; height: 340px;
    background: linear-gradient(180deg, rgba(120,100,90,0.55) 0%, #2a2a33 45%, #1b1b22 100%);
  }
  .performer-credit {
    position: absolute;
    left: 0; top: 792px;
    width: 800px;
    text-align: center;
    color: var(--white);
    font-size: 26px;
    line-height: 32px;
  }
  .schedule-band {
    position: absolute;
    left: 0; top: 843px;
    width: 800px; height: 177px;
    background: linear-gradient(90deg, var(--band-dark) 0%, var(--band-warm) 25%, #6a3a14 50%, var(--band-warm) 75%, var(--band-dark) 100%);
  }
  .schedule-text {
    position: absolute;
    left: 0; top: 858px;
    width: 800px;
    text-align: center;
    color: var(--white);
  }
  .schedule-text .day { font-size: 48px; line-height: 58px; }
  .schedule-text .time { font-size: 32px; line-height: 38px; }
  .venue-photo {
    position: absolute;
    left: 627px; top: 980px;
    width: 173px; height: 220px;
    background: linear-gradient(180deg, #3b2520 0%, #7a2a2a 55%, #c9c2bc 100%);
  }
  .venue {
    position: absolute;
    left: 114px; top: 1068px;
    width: 620px;
    text-align: center;
    color: var(--gold);
    font-size: 31px;
    line-height: 43px;
    font-style: normal;
    white-space: nowrap;
  }
  .venue .street { color: var(--gold-bright); }
</style>
</head>
<body>
  <main class="poster">
    <div class="mandala-ornament" role="img" aria-label="Circular mandala ornament of magenta butterflies and golden flowers"></div>
    <div class="devotional-illustration" role="img" aria-label="Painted devotional figure holding prayer beads"></div>

    <h1 class="headline">
      <span class="word free">Free</span>
      <span class="kirtan">Kirtan</span>
      <span class="word experience">Experience</span>
    </h1>

    <div class="performer-photo" role="img" aria-label="Musician singing into a microphone while playing acoustic guitar"></div>
    <p class="performer-credit">Madhava Vani Prabhu &amp; Friends</p>

    <div class="schedule-band" role="img" aria-label="Candlelit room with drums"></div>
    <div class="schedule-text">
      <p class="day">EVERY FRIDAY NIGHT</p>
      <p class="time">7:00 PM TO 8:30 PM</p>
    </div>

    <div class="venue-photo" role="img" aria-label="Singer with raised hand, eyes closed in devotion"></div>
    <address class="venue">
      <span class="name">Nohea Breath &amp; Movement Loft</span><br>
      <span class="street">752 Wenmore St. Paia</span>
    </address>
  </main>
</body>
</html>
```